International tradind company needs a professional Business Card

We are an international trading company and we need a business card for our CEO and employers so they can give it away in their meetings and while networking.
We want the card design quality to cause an immediate "wow" and we count on you to do that!

key-words and concepts to communicate: trustworthiness, ethics, sucess, modern, global business, networking

Our favorite colours are blue and grey but we are open to suggestions.

It would be recommended that our logo was part of the card. You can see it in www.velmarholding.com . We also would like the following info on the card:
Name
position in the company
cell phone and personal email

```html
<!DOCTYPE html>
<html lang="en">
<head>
<meta charset="utf-8">
<title>Velmar Group – Business Card</title>
<link href="https://fonts.googleapis.com/css2?family=Open+Sans:wght@400&family=Questrial&display=swap" rel="stylesheet">
<style>
  :root {
    --backdrop: #d9d9d6;
    --card-dark: #000000;
    --card-light: #ffffff;
    --brand-navy: #1f1a5c;
    --brand-blue: #3b7fc6;
    --text-ink: #1a1a1a;
    --rule-grey: #8a8a8a;
    --on-dark: #ffffff;
  }
  * { margin: 0; padding: 0; box-sizing: border-box; }
  html, body {
    width: 1200px; height: 900px; overflow: hidden;
    background: var(--backdrop);
  }
  .canvas { position: relative; width: 1200px; height: 900px; }
  .card {
    position: absolute; top: 148px;
    width: 375px; height: 640px;
    border-radius: 18px;
    overflow: hidden;
  }
  .card--back { left: 195px; background: var(--card-dark); }
  .card--front { left: 648px; background: var(--card-light); }

  .brand { position: absolute; font-family: "Open Sans", sans-serif; }
  .brand__mark {
    position: absolute; border-radius: 50%;
  }
  .brand__name {
    position: absolute; white-space: nowrap;
    font-size: 33px; font-weight: 400; line-height: 1;
  }
  .brand__tagline {
    position: absolute; white-space: nowrap;
    font-size: 19px; line-height: 1;
  }

  .card--back .brand__mark { left: 24px; top: 480px; width: 100px; height: 100px; background: var(--on-dark); }
  .card--back .brand__name { left: 146px; top: 502px; color: var(--on-dark); }
  .card--back .brand__tagline { left: 148px; top: 540px; color: var(--on-dark); }

  .card--front .brand__mark { left: 26px; top: 44px; width: 100px; height: 100px; background: var(--brand-navy); }
  .card--front .brand__name { left: 148px; top: 67px; color: var(--brand-navy); }
  .card--front .brand__tagline { left: 149px; top: 105px; color: var(--brand-blue); }

  .contact {
    position: absolute; left: 0; width: 100%;
    text-align: center;
    font-family: "Questrial", sans-serif;
    color: var(--text-ink);
    font-size: 15px; line-height: 21px;
  }
  .contact__name { font-size: 17px; font-weight: 700; letter-spacing: 0.3px; }
  .contact--person { top: 278px; }
  .contact--person .contact__role { margin-bottom: 20px; }
  .divider {
    position: absolute; left: 72px; top: 457px;
    width: 232px; height: 1px; background: var(--rule-grey);
  }
  .contact--office { top: 476px; }
  .contact--office .gap { margin-top: 20px; }
</style>
</head>
<body>
<main class="canvas">
  <section class="card card--back" aria-label="Card back">
    <div class="brand">
      <span class="brand__mark"></span>
      <span class="brand__name">Velmar Group</span>
      <span class="brand__tagline">Business Services</span>
    </div>
  </section>

  <section class="card card--front" aria-label="Card front">
    <div class="brand">
      <span class="brand__mark"></span>
      <span class="brand__name">Velmar Group</span>
      <span class="brand__tagline">Business Services</span>
    </div>

    <div class="contact contact--person">
      <p class="contact__name">Marco Reis</p>
      <p class="contact__role">CEO</p>
      <p>+351 910457283</p>
      <p>marco@velmarholding.com</p>
    </div>

    <div class="divider"></div>

    <div class="contact contact--office">
      <p>Rua das Flores, 18, 2o Esq</p>
      <p>1200-195 Lisboa</p>
      <p class="gap">T: +351 210457300</p>
      <p class="gap">contact@velmarholding.com</p>
      <p>www.velmarholding.com</p>
    </div>
  </section>
</main>
</body>
</html>
```